Darrow Consulting needs a quality & professional business card!

I am a recruitment and employment consultant from Brisbane, Australia and I had a fantastic logo organised by this community to I am hoping the business card will be the same.

I have attached the Darrow consulting logo that ideally would feature on the back of the business card. There are a number of logos for you to use as you see fit. I would like the colour cheme to match that of the Darrow Consulting logo. I also have a secondary company called Career Lantern Australia and I have included that logo as well. While it is an important part of the business I don't want this logo feature too predominantly as I am moving out of this space. This logo was created by myself and is of low quality. Feel free to use the icon and words however you want. The winning design will be smart, professional and eye-catching.

The information I am looking for in the business card is:
Name: Gavin Darrow
Position: Founder & Director
Phone: (07) 3519 6482
Mobile: 0431 586 207
Email: gavin@careerlantern.com.au

Target Market(s)

Recruiters, government, large companies

Contact Information for Business Card

Name: Gavin Darrow
Phone: (07) 3519 6482
Mobile: 0431 586 207
Web: www.careerlantern.com.au

Font styles to use
Serif
Sans Serif

Requirements
Must have
• Darrow Consulting Logo on reverse side
• Contact details on front side with smaller reference to Darrow Consulting logo and Career Lantern Australia logo

```html
<!DOCTYPE html>
<html lang="en">
<head>
<meta charset="utf-8">
<title>Darrow Consulting — Business Card</title>
<link href="https://fonts.googleapis.com/css2?family=Roboto:wght@400;500;700&display=swap" rel="stylesheet">
<style>
  :root {
    --backdrop: #2e2e2e;
    --card: #ffffff;
    --blue: #0a93cf;
    --orange: #e0822f;
    --orange-fold: #9a531a;
    --ink: #1f2326;
    --green: #1fa64a;
  }
  * { margin: 0; padding: 0; box-sizing: border-box; }
  html, body {
    width: 1200px; height: 900px; overflow: hidden;
    background: var(--backdrop);
    font-family: "Roboto", Arial, sans-serif;
  }
  .card {
    position: absolute; left: 285px; width: 630px; height: 361px;
    background: var(--card); border-radius: 14px; overflow: hidden;
  }
  .card--front { top: 50px; }
  .card--back { top: 473px; }

  .front-band { position: absolute; inset: 0; }

  .brand {
    position: absolute; display: flex; align-items: center; gap: 10px;
    color: var(--ink); font-weight: 500; white-space: nowrap;
  }
  .brand__mark { background: var(--ink); flex: none; }
  .brand--small { left: 50px; top: 56px; font-size: 24px; }
  .brand--small .brand__mark { width: 30px; height: 30px; }
  .brand--large { left: 0; right: 0; top: 150px; justify-content: center; font-size: 48px; gap: 18px; }
  .brand--large .brand__mark { width: 60px; height: 60px; }

  .name-ribbon {
    position: absolute; left: 321px; top: 32px; width: 266px; height: 62px;
  }
  .name-ribbon__shape { position: absolute; inset: 0; }
  .name-ribbon__text {
    position: absolute; left: 30px; right: 0; top: 9px; text-align: center; color: #fff;
  }
  .name-ribbon__name { font-size: 20px; font-weight: 500; line-height: 1.2; }
  .name-ribbon__title { font-size: 12px; margin-top: 3px; }

  .secondary {
    position: absolute; left: 33px; top: 182px; color: var(--ink);
  }
  .secondary__name { font-size: 15px; font-weight: 700; line-height: 1; }
  .secondary__region { font-size: 7px; font-weight: 400; margin-top: 2px; }

  .contacts { position: absolute; left: 33px; top: 232px; list-style: none; }
  .contacts li {
    display: flex; align-items: center; height: 25.5px; font-size: 14.5px; color: var(--ink);
  }
  .contacts svg { width: 20px; height: 20px; margin-right: 14px; flex: none; }

  .address {
    position: absolute; left: 348px; width: 220px; top: 267px; text-align: center;
    color: #fff; font-size: 14px; line-height: 18px;
  }
  .address svg { display: block; margin: 0 auto 10px; }

  .back-web {
    position: absolute; left: 0; right: 0; top: 323px; text-align: center;
    font-size: 14px; color: var(--ink);
  }
</style>
</head>
<body>

<section class="card card--front">
  <svg class="front-band" width="630" height="361" viewBox="0 0 630 361">
    <polygon points="371,0 630,0 630,361 267,361" fill="var(--blue)"/>
    <polygon points="321,94 343,94 336,125" fill="var(--orange-fold)"/>
  </svg>

  <div class="brand brand--small"><span class="brand__mark"></span>Darrow Consulting</div>

  <div class="name-ribbon">
    <svg class="name-ribbon__shape" width="266" height="62" viewBox="0 0 266 62">
      <polygon points="22,0 266,0 266,62 0,62" fill="var(--orange)"/>
    </svg>
    <div class="name-ribbon__text">
      <div class="name-ribbon__name">Gavin Darrow</div>
      <div class="name-ribbon__title">Founder &amp; Director</div>
    </div>
  </div>

  <div class="secondary">
    <div class="secondary__name">Career Lantern</div>
    <div class="secondary__region">Australia</div>
  </div>

  <ul class="contacts">
    <li>
      <svg viewBox="0 0 20 20"><rect width="20" height="20" fill="var(--green)"/><path d="M6 4l3 3-2 2c1 2 2 3 4 4l2-2 3 3-2 2C8 16 4 12 4 6z" fill="#fff"/></svg>
      0431 586 207
    </li>
    <li>
      <svg viewBox="0 0 20 20"><rect width="20" height="20" fill="var(--green)"/><rect x="4" y="8" width="12" height="8" rx="1.5" fill="#fff"/><path d="M3 8c2-4 12-4 14 0" stroke="#fff" stroke-width="2" fill="none"/><circle cx="10" cy="12" r="2" fill="var(--green)"/></svg>
      (07) 3519 6482
    </li>
    <li>
      <svg viewBox="0 0 20 20"><rect width="20" height="20" fill="var(--green)"/><rect x="4" y="6" width="12" height="9" fill="#fff"/><path d="M4 6l6 5 6-5M4 15l5-4M16 15l-5-4" stroke="var(--green)" stroke-width="1" fill="none"/></svg>
      gavin@careerlantern.com.au
    </li>
    <li>
      <svg viewBox="0 0 20 20"><rect width="20" height="20" fill="var(--green)"/><circle cx="10" cy="10" r="6" fill="none" stroke="#fff" stroke-width="1.6"/><path d="M4 10h12M10 4c-3 3-3 9 0 12M10 4c3 3 3 9 0 12" stroke="#fff" stroke-width="1" fill="none"/></svg>
      www.careerlantern.com.au
    </li>
  </ul>

  <div class="address">
    <svg width="12" height="16" viewBox="0 0 12 16"><path d="M6 0a6 6 0 0 1 6 6c0 4-6 10-6 10S0 10 0 6a6 6 0 0 1 6-6z" fill="#fff"/><circle cx="6" cy="6" r="2.2" fill="var(--blue)"/></svg>
    Suite 8, 47 Fernleigh Street<br>Brisbane QLD 4000
  </div>
</section>

<section class="card card--back">
  <div class="brand brand--large"><span class="brand__mark"></span>Darrow Consulting</div>
  <div class="back-web">www.careerlantern.com.au</div>
</section>

</body>
</html>
```